Lawn care business card

I am looking for a quality designed personal business card to represent the quality and elegant nature of our company. We separate ourselves in our market by the aesthetic value of our work, so I am looking for marketing material that does the same. We target our marketing high end customers, and we try to avoid price shoppers. I am open to all design options, so long as they are in line with our companies values.

We are tend to go with a retro look on everything from our logo and print material, to our uniforms. We like to portray and "old fashion" set of core values, with a modern elegance. So a wild and crazy look is out of the question.

Things I'd like on the card:
1.) Logo
2.) Phone number: (816) 555-0193
3.) Website: Verdantix.com
4.) Email: peterholloway@verdantix.com
5.) My name: Peter Holloway
6.) Facebook link: facebook.com/VerdantixGroundsandGarden
7.) Instagram: http://instagram.com/verdantix

Attached is a copy of our logo.

```html
<!DOCTYPE html>
<html lang="en">
<head>
<meta charset="utf-8">
<title>Peter Holloway — Fernwold Business Card</title>
<link href="https://fonts.googleapis.com/css2?family=Roboto+Slab:wght@300;400&display=swap" rel="stylesheet">
<style>
  :root {
    --backdrop: #d9d5cc;
    --card: #f1ecdc;
    --ink: #3b4032;
    --accent: #e4603a;
    --rule: #3b4032;
  }
  * { margin: 0; padding: 0; box-sizing: border-box; }
  html, body {
    width: 1200px; height: 800px; overflow: hidden;
    background: var(--backdrop);
  }
  .canvas { position: relative; width: 1200px; height: 800px; }
  .card {
    position: absolute; left: 100px; top: 114px;
    width: 1000px; height: 572px;
    background: var(--card);
    font-family: "Roboto Slab", Georgia, serif;
    color: var(--ink);
    box-shadow: 0 6px 18px rgba(0,0,0,0.18);
  }
  .brand {
    position: absolute; left: 70px; top: 244px;
    display: flex; align-items: center; gap: 16px;
  }
  .brand-dot {
    width: 34px; height: 34px; border-radius: 50%;
    background: var(--accent); flex: none;
  }
  .brand-name {
    font-size: 44px; font-weight: 400; letter-spacing: 3px;
    color: var(--ink); text-transform: uppercase; line-height: 1;
  }
  .website {
    position: absolute; left: 70px; bottom: 62px;
    font-size: 30px; font-weight: 400; letter-spacing: 1px;
    color: var(--accent); text-transform: uppercase; line-height: 1;
  }
  .details {
    position: absolute; left: 470px; top: 88px; width: 470px;
  }
  .person-name {
    font-size: 44px; font-weight: 400; letter-spacing: 1.5px;
    text-transform: uppercase; line-height: 1;
  }
  .double-rule {
    margin: 28px 0 24px;
    border-top: 3px solid var(--rule);
    padding-top: 4px;
  }
  .double-rule::after {
    content: ""; display: block; border-top: 1.5px solid var(--rule);
  }
  .double-rule.bottom { margin: 22px 0 0; }
  .contact-line {
    display: flex; gap: 18px;
    font-size: 22px; font-weight: 400; line-height: 1.7;
    white-space: nowrap;
  }
  .social-list { margin-top: 14px; }
  .social-line {
    display: flex; align-items: center; gap: 12px;
    font-size: 22px; font-weight: 400; margin-top: 10px;
    white-space: nowrap;
  }
  .social-marker {
    width: 30px; height: 30px; background: var(--ink); flex: none;
  }
</style>
</head>
<body>
<main class="canvas">
  <section class="card" aria-label="Business card">
    <div class="brand">
      <span class="brand-dot"></span>
      <span class="brand-name">Fernwold</span>
    </div>
    <div class="website">Fernwold.com</div>

    <div class="details">
      <h1 class="person-name">Peter Holloway</h1>
      <div class="double-rule"></div>
      <p class="contact-line"><span>(816) 555-0193</span><span>Fernwold.com</span></p>
      <p class="contact-line">peterholloway@fernwold.com</p>
      <div class="social-list">
        <p class="social-line"><span class="social-marker"></span>/FernwoldGroundsandGarden</p>
        <p class="social-line"><span class="social-marker"></span>/fernwold</p>
      </div>
      <div class="double-rule bottom"></div>
    </div>
  </section>
</main>
</body>
</html>
```